Pull Up Banner - Recruitment Company

We would like a design for a pull up banner.

For context: we are a recruitment business. We specialise in helping people in healthcare industry to find jobs in Australia.

I have come up with several ideas and text for the banner. Feel free to use the following as you see appropriate:

- Our logo (see attached)
- 'Healthcare Recruitment Agency'
- Some sort of imagine / cartoon of medical professionals (ie. doctor, nurse, physiotherapist, speech pathologist). A cartoon is more friendly than committing to a photo
- 'Empowering your next career move'
- 'Discover tailored opportunities based on your career preferences'
- Dot points (allied health, nursing, medical imaging)
- Contact info at the bottom including our website (www.quellstaffing.com.au, our Instagram handle @quellstaffing, Mobile: XXXX XXX XXX. The title section for contact information could be 'Get in touch:'

Feel free to submit a couple of designs and we can merge aspects that look good on your designs and find the perfect fit.
Thank you
Updates

Hello,

Thank you for your initial submissions to this project. I appreciate the time you've invested.

After reviewing the first attempt, I'd like to share some feedback and initial observations:

- Professionalism and engagement: Is the overall appearance of the banner professional? It's crucial that we have a high-quality design as this will represent our business.

- Image selection: The image (whether cartoon or real people) appears quite generic. Please consider submitting the banner with a few different photos in the middle for us to choose from. Ensure the image is a good fit and not simply a generic stock photo.

- Contact section: Kindly remove the phone number; we no longer wish to include it on the banner. Instead, please include our website (www.quellstaffing.com.au) and Instagram handle (@quellstaffing).

- Color scheme: White, black, and red/pink are preferred, or alternatively, blue. However, please avoid incorporating too many different colors as it may detract from the professional appearance.

We will be printing the design on a banner and require it to look professional and engaging.

Thank you once again for your submissions. I hope the feedback provided above is helpful.

Warm regards,

Target Market(s)

Allied Health Australia

Font styles to use
Serif

Colors
0054AA
0677BA
7BADD7
CADEEF
E8F1F8
0094D4
00A9DD
6FCCEA
C7EBF8
E9F6FB
EB3D1F
EC4F4E
F09395
F8D3D4
FCEDEE

```html
<!DOCTYPE html>
<html lang="en">
<head>
<meta charset="utf-8">
<title>Quell Staffing – Healthcare Recruitment Banner</title>
<link href="https://fonts.googleapis.com/css2?family=Montserrat:wght@400;500;600;700;800&display=swap" rel="stylesheet">
<style>
  :root {
    --page-bg: #e6ecf0;
    --white: #ffffff;
    --ink: #0d0d0d;
    --brand-blue: #0a6fb6;
    --band-top: #0a74bb;
    --band-bottom: #2a8fcf;
    --band-light: #4badde;
    --pale-blue: #cae4f5;
    --art-light: #e8f1f8;
    --art-mid: #cfe0ee;
  }
  * { margin: 0; padding: 0; box-sizing: border-box; }
  html, body {
    width: 1200px; height: 1200px; overflow: hidden;
    background: var(--page-bg);
    font-family: "Montserrat", Arial, sans-serif;
  }
  .banner {
    position: absolute; left: 368px; top: 30px;
    width: 464px; height: 1140px;
    background: var(--white);
    overflow: hidden;
    box-shadow: 0 6px 24px rgba(30, 60, 80, 0.18);
  }
  .brand-name {
    position: absolute; left: 45px; top: 56px;
    font-weight: 800; font-size: 26px; letter-spacing: 1px;
    color: var(--ink);
  }
  .headline {
    position: absolute; left: 38px; top: 136px;
    font-weight: 700; font-size: 57px; line-height: 56px;
    color: var(--brand-blue); letter-spacing: -0.3px;
  }
  .team-art {
    position: absolute; left: 26px; top: 318px;
    width: 414px; height: 220px;
    background: linear-gradient(180deg, var(--art-light) 0%, var(--art-mid) 100%);
    border-radius: 40px 40px 0 0;
  }
  .lower-panel { position: absolute; left: 0; top: 0; width: 464px; height: 1140px; }
  .tagline {
    position: absolute; left: 33px; top: 566px;
    font-weight: 600; font-size: 38px; line-height: 40px;
    color: var(--pale-blue);
  }
  .intro {
    position: absolute; left: 36px; top: 686px;
    font-weight: 400; font-size: 21px; line-height: 28px;
    color: var(--white);
  }
  .specialties {
    position: absolute; left: 66px; top: 762px;
    list-style: none;
  }
  .specialties li {
    display: flex; align-items: center;
    font-size: 24px; font-weight: 400; color: var(--white);
    height: 38px;
  }
  .specialties li::before {
    content: ""; width: 8px; height: 8px;
    border: 2.5px solid var(--white); border-radius: 3px;
    background: #0b4a80; margin-right: 14px;
  }
  .contact-title {
    position: absolute; left: 33px; top: 907px;
    width: 388px; height: 42px;
    background: var(--pale-blue); border-radius: 8px;
    box-shadow: 0 4px 8px rgba(0, 40, 80, 0.25);
    display: flex; align-items: center; justify-content: center;
    font-weight: 700; font-size: 23px; color: var(--brand-blue);
  }
  .contact-list { position: absolute; left: 34px; top: 974px; list-style: none; }
  .contact-list li {
    display: flex; align-items: center; height: 46px;
    font-size: 23px; font-weight: 400; color: var(--white);
  }
  .contact-icon { width: 36px; height: 36px; margin-right: 16px; flex: none; }
</style>
</head>
<body>
  <main class="banner">
    <div class="brand-name">QUELL STAFFING</div>
    <h1 class="headline">Healthcare<br>Recruitment<br>Agency</h1>

    <div class="team-art" role="img" aria-label="Illustration of a diverse team of doctors and nurses in white coats with stethoscopes and clipboards"></div>

    <svg class="lower-panel" viewBox="0 0 464 1140" aria-hidden="true">
      <defs>
        <linearGradient id="bandGradient" x1="0" y1="0" x2="0" y2="1">
          <stop offset="0" stop-color="#0a74bb"/>
          <stop offset="1" stop-color="#2a8fcf"/>
        </linearGradient>
      </defs>
      <path d="M0 458 Q232 600 464 458 L464 1140 L0 1140 Z" fill="#0a6fb6"/>
      <path d="M0 470 Q232 606 464 470" fill="none" stroke="#ffffff" stroke-width="4"/>
      <path d="M0 476 Q232 614 464 476 L464 1140 L0 1140 Z" fill="url(#bandGradient)"/>
      <path d="M0 934 Q232 900 464 934 L464 1140 L0 1140 Z" fill="#4badde"/>
    </svg>

    <h2 class="tagline">Empowering your<br>Next career move</h2>
    <p class="intro">Discover tailored opportunities<br>Based on your career preferences</p>

    <ul class="specialties">
      <li>Medical imaging</li>
      <li>Allied health</li>
      <li>Nursing</li>
    </ul>

    <div class="contact-title">Get in touch</div>

    <ul class="contact-list">
      <li>
        <svg class="contact-icon" viewBox="0 0 36 36" fill="none" stroke="#fff" stroke-width="1.8">
          <circle cx="18" cy="18" r="16"/>
          <ellipse cx="18" cy="18" rx="7" ry="16"/>
          <line x1="2" y1="18" x2="34" y2="18"/>
          <line x1="18" y1="2" x2="18" y2="34"/>
          <path d="M5 10 H31 M5 26 H31"/>
        </svg>
        www.quellstaffing.com.au
      </li>
      <li>
        <svg class="contact-icon" viewBox="0 0 36 36" fill="none" stroke="#fff" stroke-width="2">
          <rect x="5" y="5" width="26" height="26" rx="7"/>
        </svg>
        @quellstaffing
      </li>
      <li>
        <svg class="contact-icon" viewBox="0 0 36 36" fill="none" stroke="#fff" stroke-width="1.8" stroke-linejoin="round">
          <path d="M9 4 L14 10 L11 14 Q14 21 22 25 L26 22 L32 27 L28 32 Q16 31 8 21 Q3 13 9 4 Z"/>
          <path d="M21 5 Q30 7 31 16"/>
          <path d="M20 10 Q25 11 26 16"/>
        </svg>
        XXXX XXX XXX
      </li>
    </ul>
  </main>
</body>
</html>
```